Graphic to show easy steps to find financial clarity

Howdy-I need a graphic that describe my Coin Compass Method.The attached is a concept, but please use your own creativity to show how you would display this:- There are 5 steps the process (and then we repeat/recalculate)- And three bullets that drive home the results of the processI've also attached my logo. Please use the colors in my logo and maybe add a soft green as needed.The reader should be able to briefly scan this document and understand that this is an easy/simple process that tells them how to manage their cash.Thanks!-Ned

Target Market(s)

wealthy women, whether single or married

Requirements
Must have
• Please use the colors in my logo and a soft green if needed
Should not have
• This should be a very easy to read graphic that communicates how simple/easy this is to do.

```html
<!DOCTYPE html>
<html lang="en">
<head>
<meta charset="utf-8">
<title>Coin Compass Method</title>
<link rel="stylesheet" href="https://fonts.googleapis.com/css2?family=Inter:wght@300;400&display=swap">
<style>
  :root {
    --navy: #233773;
    --navy-band: #3b4c87;
    --lavender: #d2d1e2;
    --lavender-pale: #e8e7f1;
    --stone: #dcdadc;
    --mint: #e1eee3;
    --green-band: #9ccda7;
    --graphite-band: #808080;
    --rule: #555555;
    --white: #ffffff;
  }
  html, body {
    margin: 0;
    padding: 0;
    width: 1200px;
    height: 800px;
    overflow: hidden;
    background: var(--white);
  }
  .method-graphic {
    display: block;
    width: 1200px;
    height: 800px;
    font-family: "Inter", Arial, sans-serif;
  }
  .panel-left { fill: var(--lavender); }
  .panel-right { fill: var(--lavender-pale); }
  .wheel-halo { fill: var(--white); }
  .band--navy { fill: var(--navy-band); }
  .band--graphite { fill: var(--graphite-band); }
  .band--green { fill: var(--green-band); }
  .segment { stroke: var(--white); stroke-width: 20; stroke-linejoin: miter; }
  .segment--lavender { fill: var(--lavender); }
  .segment--stone { fill: var(--stone); }
  .segment--mint { fill: var(--mint); }
  .hub { fill: var(--white); }
  .band-label {
    fill: var(--white);
    font-size: 66px;
    font-weight: 300;
    letter-spacing: 4px;
  }
  .segment-text {
    fill: var(--navy);
    font-size: 45px;
    font-weight: 300;
    text-anchor: middle;
  }
  .hub-title {
    fill: var(--navy);
    font-size: 56px;
    font-weight: 400;
    text-anchor: middle;
  }
  .result-text {
    fill: var(--navy);
    font-size: 54px;
    font-weight: 300;
    text-anchor: middle;
  }
  .result-rule { stroke: var(--rule); stroke-width: 3; }
</style>
</head>
<body>
<svg class="method-graphic" viewBox="0 0 2344 1563" xmlns="http://www.w3.org/2000/svg" role="img" aria-label="Coin Compass Method: five steps and a monthly repeat, with three results">
  <defs>
    <path id="band-shape" d="M809.5 141.4 A617 617 0 0 1 1311.2 431 L1206.1 496.8 A493 493 0 0 0 805.2 265.3 Z"/>
    <path id="band-arc" d="M825 229.3 A530 530 0 0 1 1227.4 461.6"/>
    <path id="segment-shape" d="M788 568 L788 285 A473 473 0 0 1 1197.6 521.5 L952.5 663 A190 190 0 0 0 788 568 Z"/>
  </defs>

  <polygon class="panel-left" points="170,142 1405,142 1605,758 1405,1375 170,1375"/>
  <polygon class="panel-right" points="1430,142 2210,142 2210,1375 1430,1375 1630,758"/>

  <circle class="wheel-halo" cx="788" cy="758" r="645"/>

  <g class="step-bands">
    <g>
      <use class="band--navy" href="#band-shape"/>
      <text class="band-label"><textPath href="#band-arc" startOffset="50%" text-anchor="middle">STEP 1</textPath></text>
    </g>
    <g transform="rotate(60 788 758)">
      <use class="band--graphite" href="#band-shape"/>
      <text class="band-label"><textPath href="#band-arc" startOffset="50%" text-anchor="middle">STEP 2</textPath></text>
    </g>
    <g transform="rotate(120 788 758)">
      <use class="band--green" href="#band-shape"/>
      <text class="band-label"><textPath href="#band-arc" startOffset="50%" text-anchor="middle">STEP 3</textPath></text>
    </g>
    <g transform="rotate(180 788 758)">
      <use class="band--navy" href="#band-shape"/>
      <text class="band-label"><textPath href="#band-arc" startOffset="50%" text-anchor="middle">STEP 4</textPath></text>
    </g>
    <g transform="rotate(240 788 758)">
      <use class="band--graphite" href="#band-shape"/>
      <text class="band-label"><textPath href="#band-arc" startOffset="50%" text-anchor="middle">STEP 5</textPath></text>
    </g>
    <g transform="rotate(300 788 758)">
      <use class="band--green" href="#band-shape"/>
      <text class="band-label"><textPath href="#band-arc" startOffset="50%" text-anchor="middle">REPEAT</textPath></text>
    </g>
  </g>

  <g class="wheel-segments">
    <use class="segment segment--lavender" href="#segment-shape"/>
    <use class="segment segment--stone" href="#segment-shape" transform="rotate(60 788 758)"/>
    <use class="segment segment--mint" href="#segment-shape" transform="rotate(120 788 758)"/>
    <use class="segment segment--lavender" href="#segment-shape" transform="rotate(180 788 758)"/>
    <use class="segment segment--stone" href="#segment-shape" transform="rotate(240 788 758)"/>
    <use class="segment segment--mint" href="#segment-shape" transform="rotate(300 788 758)"/>
  </g>

  <circle class="hub" cx="788" cy="758" r="190"/>

  <g class="segment-labels">
    <text class="segment-text"><tspan x="973" y="435">Know</tspan><tspan x="973" y="485">your annual</tspan><tspan x="973" y="535">spending</tspan></text>
    <text class="segment-text"><tspan x="1120" y="727">Project</tspan><tspan x="1120" y="777">special</tspan><tspan x="1120" y="827">expenses</tspan></text>
    <text class="segment-text"><tspan x="973" y="1022">Add up your</tspan><tspan x="973" y="1072">5-year cash</tspan><tspan x="973" y="1122">needs</tspan></text>
    <text class="segment-text"><tspan x="600" y="1022">Set them</tspan><tspan x="600" y="1072">aside in</tspan><tspan x="600" y="1122">savings</tspan></text>
    <text class="segment-text"><tspan x="453" y="752">Invest</tspan><tspan x="453" y="802">the rest</tspan></text>
    <text class="segment-text"><tspan x="600" y="460">Recalculate</tspan><tspan x="600" y="510">monthly</tspan></text>
  </g>

  <text class="hub-title"><tspan x="788" y="712">COIN</tspan><tspan x="788" y="777">COMPASS</tspan><tspan x="788" y="842">METHOD</tspan></text>

  <g class="results">
    <text class="result-text"><tspan x="1905" y="440">Know your lifestyle</tspan><tspan x="1905" y="502">will be unaffected</tspan><tspan x="1905" y="564">by the markets for</tspan><tspan x="1905" y="626">at least 5 years</tspan></text>
    <line class="result-rule" x1="1835" y1="686" x2="1975" y2="686"/>
    <text class="result-text"><tspan x="1905" y="780">Spend intentionally</tspan><tspan x="1905" y="842">and with joy</tspan></text>
    <line class="result-rule" x1="1835" y1="902" x2="1975" y2="902"/>
    <text class="result-text"><tspan x="1905" y="995">Create a solid base</tspan><tspan x="1905" y="1057">for lifetime cash</tspan><tspan x="1905" y="1119">projections</tspan></text>
  </g>
</svg>
</body>
</html>
```